continued... Web Design for Professional Development and marketplace

in addition to the homepages that you are desiging, can you also create designs for the attached wireframes that are part of the same website.
I am creating this as a seperate project as we are keen to see your designs for the rest of the website.
VIdeo of prototype and homepage designs
https://www.quellbin.net/sh/rk8tp2mqvx41hwa/7Gt3oLnQ2z/design
Updates
added an additional wireframe that was missed in the original upload
added one more wireframe for the homepage: where the user is prompted to login or signup
Industry/Entity Type
Marketplace
Look and feel
Each slider illustrates characteristics of the customer's brand and the style your logo design should communicate.

```html
<!DOCTYPE html>
<html lang="en">
<head>
<meta charset="utf-8">
<title>Professional Development Marketplace</title>
<link rel="stylesheet" href="https://fonts.googleapis.com/css2?family=Roboto:wght@400;500;700&family=Roboto+Condensed:wght@700&display=swap">
<style>
:root{
  --page:#f2f2f2;
  --dark:#3d3d3d;
  --green:#38946c;
  --green-alt:#42a37a;
  --mint:#dff1e8;
  --white:#ffffff;
  --ink:#222222;
  --muted:#555555;
  --star-off:#8a9a93;
  --link:#1a1aee;
}
*{box-sizing:border-box;margin:0;padding:0}
html,body{width:1200px;height:824px;overflow:hidden;background:var(--page);font-family:"Roboto",sans-serif;color:var(--ink)}
.site{position:relative;width:1200px;height:824px}
.abs{position:absolute}

.topbar{left:246px;top:26px;width:700px;height:51px;background:var(--dark)}
.menu-btn{left:10px;top:9px;width:33px;height:33px;background:var(--green);display:flex;flex-direction:column;justify-content:center;gap:3px;padding:0 6px}
.menu-btn span{display:block;height:2px;background:var(--white)}
.search{left:53px;top:9px;width:163px;height:33px;background:var(--white);display:flex;align-items:center;justify-content:space-between;padding:0 6px 0 14px;font-size:12px}
.brand{left:243px;top:7px;color:var(--white);line-height:1}
.brand-main{font-size:24px;font-weight:400;letter-spacing:.3px}
.brand-sub{font-size:11px;margin-top:1px}
.head-btn{top:9px;height:33px;background:var(--white);display:flex;align-items:center;gap:6px;padding:0 8px;font-size:12px;line-height:1.05}
.btn-add{left:403px;width:81px}
.btn-login{left:506px;width:82px;padding-left:10px}
.btn-signup{left:609px;width:81px;justify-content:center}

.subnav{left:246px;top:77px;width:700px;height:26px;background:var(--mint);font-size:10px;color:var(--muted)}
.subnav span{position:absolute;top:7px}
.subnav .strong{font-weight:500}

.filters{left:246px;top:103px;width:700px;height:51px;display:flex}
.filter{height:100%;color:var(--white);text-align:center;padding-top:10px;background:var(--green)}
.filter:nth-child(even){background:var(--green-alt)}
.filter b{display:block;font-weight:400;font-size:12px}
.filter small{display:block;font-size:8px;margin-top:8px;opacity:.9}

.hero{left:246px;top:154px;width:700px;height:232px;background:linear-gradient(100deg,#b9c6cc 0%,#dfe7ea 35%,#eef3f4 60%,#c9dbe0 100%)}
.hero h1{position:absolute;top:27px;width:100%;text-align:center;font-family:"Roboto Condensed",sans-serif;font-size:26px;color:#111;letter-spacing:-.3px}
.social-btn{left:73px;top:114px;width:238px;height:34px;background:#2e6d9c;color:var(--white);display:flex;align-items:center;box-shadow:0 8px 8px -6px rgba(0,0,0,.35)}
.social-btn .mark{width:38px;height:100%;border-right:1px solid #1f5680;display:flex;align-items:center;justify-content:center}
.social-btn .mark i{width:14px;height:14px;background:var(--white);display:block}
.social-btn .label{padding-left:18px;font-size:16px;letter-spacing:.3px}
.divider{left:354px;top:83px;width:1px;height:99px;background:#8f9a9e}
.input{left:394px;width:270px;height:23px;background:var(--white);border:1px solid #a9b1b4;font-size:11px;color:#888;padding:4px 7px}
.forgot{left:394px;top:157px;font-size:10px;color:var(--link);text-decoration:underline}
.signin{left:569px;top:152px;width:95px;height:23px;background:var(--green);color:var(--white);font-size:11px;display:flex;align-items:center;justify-content:center}
.create{top:202px;width:100%;text-align:center;font-size:12px;color:var(--link);text-decoration:underline}

.sortbar{left:246px;top:386px;width:700px;height:50px;background:var(--dark);color:var(--white)}
.sort-label{left:17px;top:16px;font-size:13px}
.sort-select{left:56px;top:8px;width:184px;height:34px;background:var(--white);color:#444;font-size:13px;padding:9px 9px}
.view-btn{top:8px;width:83px;height:34px;background:var(--green);display:flex;align-items:center;gap:14px;padding-left:7px;font-size:13px}

.add-tile{left:246px;top:455px;width:161px;height:138px;background:var(--green);color:var(--white);text-align:center;box-shadow:0 14px 10px -10px rgba(0,0,0,.35)}
.add-tile h2{font-size:18px;font-weight:700;margin-top:20px}
.card{top:455px;width:160px;height:276px;background:var(--white);border:1px solid var(--green);text-align:center;box-shadow:0 14px 10px -10px rgba(0,0,0,.35)}
.provider-mark{position:absolute;top:14px;left:0;width:100%;height:38px;display:flex;align-items:center;justify-content:center;gap:6px;color:#1d2a5c;font-size:12px;font-weight:500;line-height:1.05;text-align:left}
.provider-mark i{width:14px;height:14px;background:#1d2a5c;display:block;flex:none}
.course{position:absolute;top:68px;width:100%;color:var(--green);font-weight:700;font-size:12.5px;line-height:16px;letter-spacing:.4px}
.org{position:absolute;width:100%;font-size:11.5px;color:#333;line-height:18px;letter-spacing:.2px}
.stars{position:absolute;top:147px;left:0;width:100%;text-align:center}
.icons{position:absolute;top:187px;left:0;width:100%;display:flex;justify-content:center;gap:10px;align-items:center}
.price{position:absolute;top:213px;width:100%;font-size:11px;color:#777}
.register{position:absolute;top:235px;left:32px;width:96px;height:23px;background:var(--green);color:var(--white);font-size:11.5px;display:flex;align-items:center;justify-content:center}
</style>
</head>
<body>
<div class="site">

  <header class="topbar abs">
    <div class="menu-btn abs"><span></span><span></span><span></span><span></span></div>
    <div class="search abs">Search
      <svg width="22" height="22" viewBox="0 0 22 22"><circle cx="9" cy="9" r="7" fill="none" stroke="#111" stroke-width="2.4"/><line x1="14" y1="14" x2="20" y2="20" stroke="#111" stroke-width="2.8"/></svg>
    </div>
    <div class="brand abs"><div class="brand-main">Professional</div><div class="brand-sub">Development Marketplace</div></div>
    <div class="head-btn btn-add abs">
      <svg width="16" height="16" viewBox="0 0 16 16"><rect x="6" y="0" width="4" height="16" fill="#222"/><rect x="0" y="6" width="16" height="4" fill="#222"/></svg>
      <span>Add<br>Review</span>
    </div>
    <div class="head-btn btn-login abs">
      <svg width="14" height="15" viewBox="0 0 14 15"><circle cx="7" cy="4" r="4" fill="#333"/><path d="M0 15c0-5 3-6.5 7-6.5s7 1.5 7 6.5z" fill="#333"/></svg>
      <span>Login</span>
    </div>
    <div class="head-btn btn-signup abs">Sign up</div>
  </header>

  <nav class="subnav abs">
    <span class="strong" style="left:219px">About</span>
    <span class="strong" style="left:276px">Business</span>
    <span class="strong" style="left:348px">Developers</span>
    <span style="left:482px">Privacy &amp; Terms</span>
    <span style="left:581px">Copyright &amp; Trademark</span>
  </nav>

  <div class="filters abs">
    <div class="filter" style="width:71px"><b>Save</b><small style="font-size:16px;margin-top:4px">+</small></div>
    <div class="filter" style="width:76px"><b>Career</b><small>(all)</small></div>
    <div class="filter" style="width:108px"><b>Specialization</b><small>(all)</small></div>
    <div class="filter" style="width:82px"><b>Location</b><small>(Vancouver)</small></div>
    <div class="filter" style="width:60px"><b>Price</b><small>($600-3000)</small></div>
    <div class="filter" style="width:96px"><b>Start Date</b><small>(2 - 6 months)</small></div>
    <div class="filter" style="width:60px"><b>Level</b><small>(intermediate)</small></div>
    <div class="filter" style="width:72px"><b>Type</b><small>(multiple)</small></div>
    <div class="filter" style="width:75px"><b>Provider</b><small>(one)</small></div>
  </div>

  <section class="hero abs" role="img" aria-label="Blurred photo of a professional in an office">
    <h1>SAVE YOUR SEARCH BY LOGGING IN NOW</h1>
    <div class="social-btn abs"><div class="mark"><i></i></div><div class="label">Sign in with ProNet</div></div>
    <div class="divider abs"></div>
    <div class="input abs" style="top:91px">Email addresss</div>
    <div class="input abs" style="top:122px">Password</div>
    <div class="forgot abs">Forget Password?</div>
    <div class="signin abs">Sign in</div>
    <div class="create abs">or, Create account..</div>
  </section>

  <div class="sortbar abs">
    <span class="sort-label abs">Sort</span>
    <div class="sort-select abs">Trending</div>
    <div class="view-btn abs" style="left:516px">
      <svg width="18" height="18" viewBox="0 0 18 18" fill="#fff"><rect width="8" height="8"/><rect x="10" width="8" height="8"/><rect y="10" width="8" height="8"/><rect x="10" y="10" width="8" height="8"/></svg>Grid
    </div>
    <div class="view-btn abs" style="left:608px">
      <svg width="24" height="18" viewBox="0 0 24 18" fill="#fff"><rect width="24" height="2.5"/><rect y="5" width="24" height="2.5"/><rect y="10" width="24" height="2.5"/><rect y="15" width="24" height="2.5"/></svg>List
    </div>
  </div>

  <div class="add-tile abs">
    <h2>Add Review</h2>
    <svg width="72" height="72" viewBox="0 0 72 72" style="margin-top:8px"><circle cx="36" cy="36" r="32" fill="none" stroke="#fff" stroke-width="7"/><rect x="31" y="16" width="10" height="40" fill="#fff"/><rect x="16" y="31" width="40" height="10" fill="#fff"/></svg>
  </div>

  <svg width="0" height="0" style="position:absolute">
    <defs>
      <polygon id="star" points="8,0 10,5.6 16,5.8 11.2,9.4 13,15.2 8,11.8 3,15.2 4.8,9.4 0,5.8 6,5.6"/>
      <g id="heart"><path d="M14 26 C2 17 1 12 1 8.5 A6.5 6.5 0 0 1 14 6 A6.5 6.5 0 0 1 27 8.5 C27 12 26 17 14 26Z" fill="none" stroke="#38946c" stroke-width="2"/></g>
      <g id="group" fill="#38946c"><circle cx="8" cy="5" r="4"/><circle cx="17" cy="5" r="4"/><path d="M0 17c0-5 3-7 8-7s8 2 8 7z"/><path d="M10 17c0-5 2-7 7-7s8 2 8 7z"/></g>
    </defs>
  </svg>

  <article class="card abs" style="left:426px">
    <div class="provider-mark"><i></i><span>Keystone<br>Practice</span></div>
    <div class="course">Product Management<br>Foundations</div>
    <div class="org" style="top:112px">Keystone Practice</div>
    <div class="stars"><svg width="92" height="16" fill="#38946c"><use href="#star" x="0"/><use href="#star" x="19"/><use href="#star" x="38"/><use href="#star" x="57"/><use href="#star" x="76" fill="#8a9a93"/></svg></div>
    <div class="icons"><svg width="28" height="27"><use href="#heart"/></svg><svg width="26" height="18"><use href="#group"/></svg></div>
    <div class="price">$995</div>
    <div class="register">Register</div>
  </article>

  <article class="card abs" style="left:606px">
    <div class="provider-mark"><i></i><span>Harbourline<br>School of Business</span></div>
    <div class="course">Product Management</div>
    <div class="org" style="top:88px">Harbourline School of<br>Business</div>
    <div class="stars"><svg width="92" height="16" fill="#38946c"><use href="#star" x="0"/><use href="#star" x="19"/><use href="#star" x="38"/><use href="#star" x="57" fill="#8a9a93"/><use href="#star" x="76" fill="#8a9a93"/></svg></div>
    <div class="icons"><svg width="28" height="27"><use href="#heart"/></svg><svg width="26" height="18"><use href="#group"/></svg></div>
    <div class="price">$3,285</div>
    <div class="register">Register</div>
  </article>

  <article class="card abs" style="left:786px">
    <div class="provider-mark"><i></i><span>Keystone<br>Practice</span></div>
    <div class="course">Product Management<br>Foucus</div>
    <div class="org" style="top:112px">Keystone Practice</div>
    <div class="stars"><svg width="92" height="16" fill="#38946c"><use href="#star" x="0"/><use href="#star" x="19"/><use href="#star" x="38"/><use href="#star" x="57"/><use href="#star" x="76"/></svg></div>
    <div class="icons" style="gap:6px">
      <svg width="28" height="27"><use href="#heart"/></svg>
      <svg width="20" height="16" viewBox="0 0 20 16"><path d="M1 11 L11 2 L19 5 L9 14Z" fill="none" stroke="#38946c" stroke-width="2"/><path d="M1 11 L9 14 L9 16 L1 13Z" fill="#38946c"/></svg>
      <svg width="26" height="18"><use href="#group"/></svg>
      <svg width="20" height="18" viewBox="0 0 20 18"><rect x="1" y="1" width="18" height="12" fill="none" stroke="#38946c" stroke-width="2"/><rect x="8" y="13" width="4" height="3" fill="#38946c"/><rect x="5" y="16" width="10" height="2" fill="#38946c"/></svg>
    </div>
    <div class="price">$995</div>
    <div class="register">Register</div>
  </article>

</div>
</body>
</html>
```